Home Equity Lines of Credit
are BACK!!!

* Up to 97.5% on Owner Occupied Properties
* 700 Minimum Scores
* Fund in only 2-3 weeks

Can be used for...
* Education Expense
* Bill Consolidation
* Home Improvement
* Investments

Call today for more information!
(800) 647-2915

Bluecrest Lending Partners, Inc.
NMLS #318660
www.bluecrestlendhub.com

```html
<!DOCTYPE html>
<html lang="en">
<head>
<meta charset="utf-8">
<title>Home Equity Lines of Credit – Bluecrest Lending Partners</title>
<link href="https://fonts.googleapis.com/css2?family=Bebas+Neue&family=Roboto:wght@400;500;700&display=swap" rel="stylesheet">
<style>
  :root {
    --brand-blue: #21619a;
    --brand-gold: #938c3c;
    --ink-dark: #1c1b22;
    --headline-ink: #141414;
    --paper: #e9eaec;
    --white: #ffffff;
    --page-bg: #d6d6d6;
  }
  * { margin: 0; padding: 0; box-sizing: border-box; }
  html, body {
    width: 1180px; height: 1200px; overflow: hidden;
    background: var(--page-bg);
  }
  .flyer {
    position: absolute; left: 40px; top: 44px;
    width: 1100px; height: 1111px;
    overflow: hidden;
    background: var(--paper);
    font-family: "Roboto", Arial, sans-serif;
    color: var(--white);
  }
  .flyer-shapes { position: absolute; inset: 0; width: 100%; height: 100%; }

  .headline {
    position: absolute; left: 76px; top: 60px;
    font-family: "Bebas Neue", "Oswald", sans-serif;
    font-size: 82px; line-height: 76px; letter-spacing: 4px;
    color: var(--headline-ink);
    font-weight: 400;
  }

  .brand {
    position: absolute; left: 812px; top: 80px;
    display: flex; align-items: center; gap: 10px;
  }
  .brand-dot { width: 30px; height: 30px; border-radius: 50%; background: var(--brand-gold); flex: none; }
  .brand-name {
    font-family: "Roboto", Arial, sans-serif; font-weight: 700;
    font-size: 17px; line-height: 1.2; color: var(--brand-blue);
    width: 200px;
  }

  .stat {
    position: absolute; transform: translateX(-50%);
    text-align: center; white-space: nowrap;
  }
  .stat-kicker, .stat-label {
    font-size: 15px; font-weight: 500; letter-spacing: 3px; line-height: 19px;
  }
  .stat-value {
    font-family: "Bebas Neue", "Oswald", sans-serif;
    font-size: 120px; line-height: 96px; letter-spacing: 1px;
  }
  .stat-ltv { left: 215px; top: 686px; }
  .stat-score { left: 567px; top: 714px; }
  .stat-score .stat-value { padding-bottom: 4px; }
  .stat-funding { left: 925px; top: 702px; }

  .uses {
    position: absolute; left: 92px; top: 896px;
    list-style: none;
  }
  .uses li {
    display: flex; align-items: center; gap: 10px;
    height: 34.7px;
    font-size: 19px; font-weight: 500; letter-spacing: 2.4px;
  }
  .uses svg { width: 22px; height: 22px; flex: none; }

  .contact {
    position: absolute; right: 102px; top: 892px;
    text-align: right; width: 330px;
  }
  .contact-company { font-size: 18px; font-weight: 500; letter-spacing: 1.2px; line-height: 26px; }
  .contact-nmls { font-size: 18px; font-weight: 700; letter-spacing: 2px; line-height: 26px; }
  .contact-rule { height: 1px; background: rgba(255,255,255,.8); margin: 10px 0 6px auto; width: 310px; }
  .contact-cta { font-size: 13px; font-weight: 500; letter-spacing: 1.6px; line-height: 18px; }
  .contact-phone {
    font-family: "Bebas Neue", "Oswald", sans-serif;
    font-size: 54px; line-height: 50px; letter-spacing: 3px;
  }

  .web-address {
    position: absolute; left: 0; right: 0; top: 1058px;
    text-align: center;
    font-size: 28px; font-weight: 500; letter-spacing: 6px;
  }
</style>
</head>
<body>
<main class="flyer">
  <svg class="flyer-shapes" viewBox="0 0 1015 1025" preserveAspectRatio="none" aria-hidden="false">
    <defs>
      <linearGradient id="roomTone" x1="0" y1="0" x2="1" y2="1">
        <stop offset="0" stop-color="#d9dadc"/>
        <stop offset="0.5" stop-color="#eeeff1"/>
        <stop offset="1" stop-color="#e2e3e6"/>
      </linearGradient>
      <radialGradient id="portraitTone" cx="0.5" cy="0.45" r="0.55">
        <stop offset="0" stop-color="#a9785c"/>
        <stop offset="0.45" stop-color="#4a3a33"/>
        <stop offset="1" stop-color="#2a2a2c" stop-opacity="0"/>
      </radialGradient>
      <linearGradient id="kitchenTone" x1="0" y1="0" x2="0" y2="1">
        <stop offset="0" stop-color="#eceae6"/>
        <stop offset="0.55" stop-color="#9aa3b3"/>
        <stop offset="1" stop-color="#d7c3a4"/>
      </linearGradient>
      <linearGradient id="graduateTone" x1="0" y1="0" x2="0" y2="1">
        <stop offset="0" stop-color="#e4e2e4"/>
        <stop offset="0.5" stop-color="#6a4436"/>
        <stop offset="1" stop-color="#1d1a1c"/>
      </linearGradient>
    </defs>

    <g role="img" aria-label="Photo of a smiling woman with curly hair and glasses resting her chin on her hand in a bright room">
      <rect width="1015" height="620" fill="url(#roomTone)"/>
      <ellipse cx="670" cy="320" rx="230" ry="290" fill="url(#portraitTone)"/>
    </g>

    <path d="M0 445 C150 430 300 470 450 510 C600 555 760 590 820 470 C860 380 900 330 1015 318 L1015 1025 L0 1025 Z" fill="var(--brand-gold)"/>
    <path d="M0 508 C150 492 300 520 450 560 C600 600 760 640 830 560 C875 500 895 385 1015 372 L1015 1025 L0 1025 Z" fill="var(--brand-blue)"/>

    <line x1="378" y1="650" x2="378" y2="795" stroke="#ffffff" stroke-opacity=".7" stroke-width="1.5"/>
    <line x1="687" y1="650" x2="687" y2="795" stroke="#ffffff" stroke-opacity=".7" stroke-width="1.5"/>

    <rect x="0" y="808" width="1015" height="150" fill="var(--brand-gold)"/>
    <path d="M0 808 L460 808 L535 883 L460 958 L0 958 Z" fill="var(--ink-dark)"/>
    <rect x="0" y="958" width="1015" height="67" fill="var(--brand-blue)"/>

    <circle cx="226" cy="448" r="160" fill="#ffffff"/>
    <circle cx="226" cy="448" r="153" fill="url(#kitchenTone)" role="img" aria-label="Photo of a couple choosing flooring samples at a kitchen counter"/>
    <circle cx="498" cy="521" r="90" fill="#ffffff"/>
    <circle cx="498" cy="521" r="83" fill="url(#graduateTone)" role="img" aria-label="Photo of a smiling graduate in a cap"/>
  </svg>

  <h1 class="headline">Home Equity<br>Lines of Credit<br>are Back!!!</h1>

  <div class="brand">
    <span class="brand-dot"></span>
    <span class="brand-name">Bluecrest Lending Partners, Inc.</span>
  </div>

  <section class="stat stat-ltv">
    <p class="stat-kicker">UP TO</p>
    <p class="stat-value">97.5%</p>
    <p class="stat-label">ON OWNER OCCUPIED<br>PROPERTIES</p>
  </section>
  <section class="stat stat-score">
    <p class="stat-value">700</p>
    <p class="stat-label">MINIMUM<br>SCORES</p>
  </section>
  <section class="stat stat-funding">
    <p class="stat-kicker">FUND IN ONLY</p>
    <p class="stat-value">2-3</p>
    <p class="stat-label">WEEKS</p>
  </section>

  <ul class="uses">
    <li><svg viewBox="0 0 22 22"><circle cx="11" cy="11" r="10" fill="#2c73b3"/><path d="M6.5 11.5 L9.6 14.5 L15.5 7.5" fill="none" stroke="#fff" stroke-width="2.2" stroke-linecap="round" stroke-linejoin="round"/></svg>EDUCATION EXPENSE</li>
    <li><svg viewBox="0 0 22 22"><circle cx="11" cy="11" r="10" fill="#2c73b3"/><path d="M6.5 11.5 L9.6 14.5 L15.5 7.5" fill="none" stroke="#fff" stroke-width="2.2" stroke-linecap="round" stroke-linejoin="round"/></svg>BILL CONSOLIDATION</li>
    <li><svg viewBox="0 0 22 22"><circle cx="11" cy="11" r="10" fill="#2c73b3"/><path d="M6.5 11.5 L9.6 14.5 L15.5 7.5" fill="none" stroke="#fff" stroke-width="2.2" stroke-linecap="round" stroke-linejoin="round"/></svg>HOME IMPROVEMENT</li>
    <li><svg viewBox="0 0 22 22"><circle cx="11" cy="11" r="10" fill="#2c73b3"/><path d="M6.5 11.5 L9.6 14.5 L15.5 7.5" fill="none" stroke="#fff" stroke-width="2.2" stroke-linecap="round" stroke-linejoin="round"/></svg>INVESTMENTS</li>
  </ul>

  <address class="contact" style="font-style:normal">
    <p class="contact-company">Bluecrest Lending Partners, Inc.</p>
    <p class="contact-nmls">NMLS #318660</p>
    <div class="contact-rule"></div>
    <p class="contact-cta">CALL TODAY FOR MORE INFORMATION!</p>
    <p class="contact-phone">(800) 647-2915</p>
  </address>

  <p class="web-address">www.bluecrestlendhub.com</p>
</main>
</body>
</html>
```